lantern-weavers - the complementary consultancy

Please create a powerpoint template for us. We are a management consultancy that combines the business aspects with the values and culture-oriented aspects (= we are a complementary consultancy).

Please also take into account the following key data:
- Logo see appendix
- Colors in the logo see appendix

I need a quick fix :))

----------------
We are a consulting company that offers its customers complementary advice for mission-critical transformation projects.

Complementary counseling integrates different perspectives and approaches to offer more comprehensive solutions and better understanding. By combining methods, models and theories from different disciplines, she supports individual needs and goals of clients or organizations.

The core idea is that connecting different approaches leads to a more comprehensive understanding and more effective solutions. It develops bespoke solutions tailored to specific needs and contexts, rather than being limited to a single theory or method.

Target Market(s)

Top management of VEK companies

Font styles to use
Other font styles liked:
• Roboto

Requirements
Must have
• PPT template including cover page, table of contents, content page, back page
Should not have
• no new logo

```html
<!DOCTYPE html>
<html lang="en">
<head>
<meta charset="utf-8">
<title>Lantern Weavers – Presentation Template</title>
<link href="https://fonts.googleapis.com/css2?family=Fira+Sans:wght@400;500;600;700&family=Open+Sans:wght@400;600;700&display=swap" rel="stylesheet">
<style>
:root{
  --bg:#d4d5d7;
  --blue:#0a70b5;
  --blue-dark:#085f9c;
  --cyan:#1aa9e6;
  --grey:#8f9194;
  --grey-light:#c5c6c8;
  --text:#222;
  --muted:#777;
  --white:#fff;
  --panel:#efeff1;
}
*{margin:0;padding:0;box-sizing:border-box}
html,body{width:1200px;height:2277px;overflow:hidden;background:var(--bg)}
body{position:relative;font-family:"Open Sans",sans-serif;color:var(--text)}
.slide{position:absolute;width:421px;height:237px;background:var(--white);overflow:hidden;box-shadow:6px 7px 10px rgba(0,0,0,.35)}
.slide.blue{background:linear-gradient(135deg,#1580c2 0%,#0a6fb3 55%,#0b67a6 100%);color:var(--white)}
.col-l{left:143px}.col-r{left:634px}
.photo{position:absolute;background:linear-gradient(160deg,#b9b5b0,#6f6a66)}
.photo.dark{background:linear-gradient(160deg,#3a3a3a,#151515)}
.photo.warm{background:linear-gradient(160deg,#c9b08e,#8d7a66)}
.illus{position:absolute;background:linear-gradient(160deg,#eef3f8,#cfdceb)}
.brand{text-align:center;font-family:"Fira Sans",sans-serif}
.brand-name{font-weight:600;font-size:21px;letter-spacing:1.5px;display:inline-flex;align-items:center;gap:7px}
.brand-tag{font-size:15px;font-weight:400;letter-spacing:.5px;margin-top:-2px}
.cover-text{text-align:center;font-family:"Fira Sans",sans-serif}
.cover-text .pre{font-size:15px}
.cover-text .name{font-size:21px;font-weight:600;line-height:1.25}
.cover-text .desc{font-size:15px}
.h-title{font-family:"Fira Sans",sans-serif;font-weight:600;color:var(--blue);position:absolute}
.tiny{font-size:5px;line-height:1.45;color:#555}
.tiny b{color:var(--blue);font-weight:600}
.btn{position:absolute;background:var(--blue);color:var(--white);font-family:"Fira Sans",sans-serif;font-size:6px;font-weight:600;border-radius:8px;width:58px;height:13px;line-height:13px;text-align:center}
.person{position:absolute;text-align:center;width:210px}
.person .nm{font-family:"Fira Sans",sans-serif;font-weight:600;color:var(--blue);font-size:15px}
.person .bar{width:18px;height:2px;background:var(--blue);margin:7px auto 8px}
.person .role{font-size:6.5px;font-weight:700}
.person .bio{font-size:5.5px;line-height:1.4;color:#444;margin-top:20px;padding:0 12px}
.group h4{font-size:5.5px;font-weight:700;margin-bottom:2px}
.group p{font-size:4px;line-height:1.45;color:#555;text-align:justify}
.legend{position:absolute;font-size:4.5px;color:#777;display:flex;gap:14px}
.legend i{display:inline-block;width:4px;height:4px;margin-right:2px}
.toc-item{position:absolute;display:flex;gap:7px;align-items:flex-start}
.toc-num{width:26px;height:26px;border-radius:50%;background:var(--blue);color:var(--white);font-family:"Fira Sans",sans-serif;font-size:10px;font-weight:600;display:flex;align-items:center;justify-content:center;box-shadow:0 0 0 2px #fff,0 0 0 3px var(--blue)}
.toc-item h5{font-size:5px;font-weight:700;margin-top:3px}
.toc-item p{font-size:4.5px;color:#888;line-height:1.5;width:110px}
</style>
</head>
<body>

<section class="slide blue col-l" style="top:91px">
  <div class="brand" style="position:absolute;top:66px;left:90px;width:290px">
    <div class="brand-name">LANTERN WEAVERS</div>
    <div class="brand-tag">complementary advisory</div>
  </div>
  <div class="cover-text" style="position:absolute;top:135px;width:421px">
    <div class="pre">Welcome to Our</div>
    <div class="name">Presentation Name</div>
    <div class="desc">Drescription</div>
  </div>
</section>

<section class="slide col-r" style="top:91px">
  <div class="brand" style="position:absolute;top:68px;left:90px;width:290px">
    <div class="brand-name" style="color:var(--blue)">LANTERN WEAVERS</div>
    <div class="brand-tag" style="color:#666">complementary advisory</div>
  </div>
  <div class="cover-text" style="position:absolute;top:137px;width:421px">
    <div class="pre">Welcome to Our</div>
    <div class="name" style="color:var(--blue)">Presentation Name</div>
    <div class="desc">Drescription</div>
  </div>
</section>

<section class="slide col-l" style="top:353px">
  <h2 class="h-title" style="left:24px;top:33px;font-size:15px">THE COMPANY</h2>
  <div class="tiny" style="position:absolute;left:24px;top:64px;width:285px">
    <p>LUMEN stands for process-oriented management of mission-critical transformation projects, in which we organize organizational change as a systemic change process in a business-motivated transformation project.</p><br>
    <p>Success makes it necessary for us to act differently together with you and your employees: Target-oriented - constructivist - transformative.</p><br>
    <p><b>Goal-oriented:</b> A successful transformation requires clear, measurable business and cultural goals of the organization, which together with the individual goals of employees and managers form the basis for defining the goals of your transformation project.</p><br>
    <p><b>Constructivist:</b> A successful transformation requires a pattern change in which your managers and employees re-evaluate and redesign the existing reality of processes, mental models or narratives. This is how cultural and structural framework conditions arise, which are essential for an agile approach. The successful introduction of agile frameworks or other process models also requires these framework conditions.</p><br>
    <p><b>Transformative:</b> A successful transformation requires an agile, value-oriented design and learning process with productively usable intermediate results as well as a communication and decision-making process in which the constructivist views of you and your employees are given sufficient space.</p>
  </div>
  <div class="illus" role="img" aria-label="Decorative illustration of stylised figures on a curved bridge" style="right:0;top:60px;width:100px;height:177px"></div>
</section>

<section class="slide blue col-r" style="top:353px">
  <div class="brand" style="position:absolute;top:68px;left:90px;width:290px">
    <div class="brand-name">LANTERN WEAVERS</div>
    <div class="brand-tag">complementary advisory</div>
  </div>
  <div style="position:absolute;left:129px;top:125px;font-family:'Fira Sans',sans-serif">
    <div style="font-size:18px;font-weight:600">Act differently for once</div>
    <div style="font-size:14px;line-height:1.3;margin-top:4px">goal oriented.<br>constructivist.<br>transformative.</div>
  </div>
</section>

<section class="slide col-l" style="top:619px">
  <div class="photo" role="img" aria-label="Portrait photo of Henrik Adler" style="left:0;top:0;width:192px;height:237px"></div>
  <div class="person" style="left:201px;top:33px">
    <div class="nm">Henrik Adler</div>
    <div class="bar"></div>
    <div class="role">Professional for agile leadership</div>
    <div class="bio">Henrik is a C-level sparring partner and turnaround manager in mission-critical transformation projects. He has complementary technical and process expertise.</div>
  </div>
  <div class="btn" style="left:277px;top:190px">Read more</div>
</section>

<section class="slide col-r" style="top:619px">
  <h2 class="h-title" style="left:30px;top:21px;font-size:15px">THE COMPANY</h2>
  <div style="position:absolute;left:30px;top:38px;font-size:7px;color:#666">Sub Heading</div>
  <div style="position:absolute;left:98px;top:42px;width:295px;height:1px;background:#ccc"></div>
  <div style="position:absolute;left:30px;top:62px;width:366px;display:grid;grid-template-columns:1fr 1fr;column-gap:26px;row-gap:12px">
    <div class="group"><h4>Group 1</h4><p>Lorem ipsum is simply dummy text of the printing and typesetting industry. Lorem ipsum has been the standard dummy text ever since the 1500s, when an unknown printer took a galley of type and scrambled it to make a type specimen book, remaining essentially unchanged.</p></div>
    <div class="group"><h4>Group 1</h4><p>Lorem ipsum is simply dummy text of the printing and typesetting industry. Lorem ipsum has been the standard dummy text ever since the 1500s, when an unknown printer took a galley of type and scrambled it to make a type specimen book, remaining essentially unchanged.</p></div>
    <div class="group"><h4>Group 1</h4><p>Lorem ipsum is simply dummy text of the printing and typesetting industry. Lorem ipsum has been the standard dummy text ever since the 1500s, when an unknown printer took a galley of type and scrambled it to make a type specimen book, remaining essentially unchanged.</p></div>
    <div class="group"><h4>Group 1</h4><p>Lorem ipsum is simply dummy text of the printing and typesetting industry. Lorem ipsum has been the standard dummy text ever since the 1500s, when an unknown printer took a galley of type and scrambled it to make a type specimen book, remaining essentially unchanged.</p></div>
    <div class="group"><h4>Group 1</h4><p>Lorem ipsum is simply dummy text of the printing and typesetting industry. Lorem ipsum has been the standard dummy text ever since the 1500s, when an unknown printer took a galley of type and scrambled it to make a type specimen book, remaining essentially unchanged.</p></div>
    <div class="group"><h4>Group 1</h4><p>Lorem ipsum is simply dummy text of the printing and typesetting industry. Lorem ipsum has been the standard dummy text ever since the 1500s, when an unknown printer took a galley of type and scrambled it to make a type specimen book, remaining essentially unchanged.</p></div>
  </div>
</section>

<section class="slide col-l" style="top:884px">
  <div class="person" style="left:0;top:34px">
    <div class="nm">Marlene K. Osterwald</div>
    <div class="bar"></div>
    <div class="role">Professional for culture and mindset change</div>
    <div class="bio">Marlene is a global cultural thought leader who works with her team as a change agent, consultant and speaker. She has brought about cultural change for various global players.</div>
  </div>
  <div class="btn" style="left:84px;top:188px">Read more</div>
  <div class="photo warm" role="img" aria-label="Portrait photo of Marlene K. Osterwald" style="right:0;top:0;width:193px;height:237px"></div>
</section>

<section class="slide col-r" style="top:884px">
  <div class="photo dark" role="img" aria-label="Portrait photo of dr Tobias Kern" style="left:0;top:0;width:193px;height:237px"></div>
  <div class="person" style="left:201px;top:36px">
    <div class="nm">dr Tobias Kern</div>
    <div class="bar"></div>
    <div class="role">Professional for Lean Agile Transition and Organizational Development</div>
    <div class="bio" style="margin-top:16px">Tobias is an expert in agile transitions and organizational development. His work focuses on modern management methods and the design and embedding of agile and hybrid methods in corporate cultures.</div>
  </div>
  <div class="btn" style="left:267px;top:191px">Read more</div>
</section>

<section class="slide col-l" style="top:1153px">
  <svg style="position:absolute;left:24px;top:30px" width="380" height="100" viewBox="0 0 380 100" role="img" aria-label="Bar chart of four series from 2018 to 2021">
    <g font-size="4.5" fill="#999" font-family="Open Sans, sans-serif">
      <text x="0" y="6">5</text><text x="0" y="21">4</text><text x="0" y="36">3</text><text x="0" y="51">2</text><text x="0" y="66">1</text><text x="0" y="81">0</text>
      <text x="50" y="90">2018</text><text x="140" y="90">2019</text><text x="230" y="90">2020</text><text x="320" y="90">2021</text>
    </g>
    <g stroke="#e3e3e3" stroke-width=".5"><line x1="8" y1="4" x2="375" y2="4"/><line x1="8" y1="19" x2="375" y2="19"/><line x1="8" y1="34" x2="375" y2="34"/><line x1="8" y1="49" x2="375" y2="49"/><line x1="8" y1="64" x2="375" y2="64"/></g>
    <line x1="8" y1="79.5" x2="375" y2="79.5" stroke="#bbb" stroke-width=".6"/>
    <g>
      <rect x="22" y="15" width="12" height="64.5" fill="var(--blue)"/><rect x="37" y="44" width="12" height="35.5" fill="var(--grey)"/><rect x="52" y="49" width="12" height="30.5" fill="var(--grey-light)"/><rect x="70" y="27" width="12" height="52.5" fill="var(--cyan)"/>
      <rect x="110" y="42" width="12" height="37.5" fill="var(--blue)"/><rect x="125" y="13" width="12" height="66.5" fill="var(--grey)"/><rect x="140" y="49" width="12" height="30.5" fill="var(--grey-light)"/><rect x="155" y="42" width="12" height="37.5" fill="var(--cyan)"/>
      <rect x="200" y="27" width="12" height="52.5" fill="var(--blue)"/><rect x="215" y="52" width="12" height="27.5" fill="var(--grey-light)"/><rect x="230" y="34" width="12" height="45.5" fill="var(--cyan)"/><rect x="245" y="19" width="12" height="60.5" fill="var(--grey)"/>
      <rect x="288" y="12" width="12" height="67.5" fill="var(--blue)"/><rect x="303" y="37" width="12" height="42.5" fill="var(--grey)"/><rect x="318" y="4" width="12" height="75.5" fill="var(--blue-dark)"/><rect x="333" y="12" width="12" height="67.5" fill="var(--grey-light)"/>
    </g>
  </svg>
  <div class="legend" style="left:56px;top:132px"><span><i style="background:var(--blue)"></i>Series A</span><span><i style="background:var(--cyan)"></i>Series B</span><span><i style="background:var(--grey)"></i>Series C</span><span><i style="background:var(--grey-light)"></i>Series D</span></div>
  <p class="tiny" style="position:absolute;left:30px;top:152px;width:366px;text-align:justify;color:#888">Lorem ipsum is simply dummy text of the printing and typesetting industry. Lorem ipsum has been the industry's standard dummy text ever since the 1500s, when an unknown printer took a galley of type and scrambled it to make a type specimen book. It has survived not only five centuries, but also the leap into electronic typesetting, remaining essentially unchanged. Lorem ipsum has been the industry's standard dummy text ever since the 1500s, when an unknown printer took a galley of type and scrambled it to make a type specimen book. It has survived not only five centuries, but also the leap into electronic typesetting, remaining essentially unchanged.</p>
</section>

<section class="slide col-r" style="top:1153px">
  <div class="illus" role="img" aria-label="Decorative illustration of stylised figures on a curved bridge" style="left:0;top:0;width:120px;height:237px"></div>
  <div style="position:absolute;left:126px;top:132px;width:280px;font-size:9px;line-height:1.45;color:#444">“ Transformation of the technical design as well as the BUILD and RUN process of the rating services for the lending business from 10 state banks in the newly founded Credit Scoring Hub (CSH) ”</div>
  <div style="position:absolute;left:126px;top:190px;width:18px;height:2px;background:var(--blue)"></div>
  <div style="position:absolute;left:126px;top:198px;font-size:9px;color:#444">Kestrel Bank: &nbsp;Jonas Weidmann, CIO</div>
</section>

<section class="slide col-l" style="top:1419px">
  <h2 class="h-title" style="left:32px;top:25px;font-size:15px">Heading Here</h2>
  <div style="position:absolute;left:32px;top:44px;font-size:7px;color:#666">Sub Heading</div>
  <div class="tiny" style="position:absolute;left:32px;top:66px;width:155px;text-align:justify;color:#888">
    <p>Lorem ipsum is simply dummy text of the printing and typesetting industry. Lorem ipsum has been the industry's standard dummy text ever since the 1500s, when an unknown printer took a galley of type and scrambled it to make a type specimen book. It has survived not only five centuries, but also the leap into electronic typesetting, remaining essentially unchanged. It was popularised in the 1960s with the release of sheets containing passages, and more recently with desktop publishing software including versions of Lorem ipsum.</p><br>
    <p>Lorem ipsum is simply dummy text of the printing and typesetting industry. Lorem ipsum has been the industry's standard dummy text ever since the 1500s, when an unknown printer took a galley of type and scrambled it to make a type specimen book.</p>
  </div>
  <svg style="position:absolute;left:253px;top:58px" width="124" height="124" viewBox="-62 -62 124 124" role="img" aria-label="Pie chart: 58%, 23%, 19%">
    <path d="M0 0 L0 -60 A60 60 0 0 1 59.5 -7.5 Z" fill="var(--cyan)"/>
    <path d="M0 0 L59.5 -7.5 A60 60 0 0 1 28.9 52.6 Z" fill="var(--grey-light)"/>
    <path d="M0 0 L28.9 52.6 A60 60 0 1 1 0 -60 Z" fill="var(--blue)"/>
    <g fill="#fff" font-size="5.5" font-weight="700" font-family="Open Sans, sans-serif">
      <text x="14" y="-37">23%</text><text x="40" y="9">19%</text><text x="-40" y="26">58%</text>
    </g>
  </svg>
  <div class="legend" style="left:242px;top:200px;color:#333;font-weight:600;gap:8px;font-size:5px"><span><i style="background:var(--blue)"></i>Sale</span><span><i style="background:var(--grey-light)"></i>Revenue</span><span><i style="background:var(--blue-dark)"></i>Profit</span><span><i style="background:var(--grey-light)"></i>Expenditure</span></div>
</section>

<section class="slide col-r" style="top:1419px">
  <h2 class="h-title" style="left:0;width:421px;text-align:center;top:27px;font-size:19px">OUR GREAT TEAM</h2>
  <div style="position:absolute;left:0;bottom:0;width:421px;height:79px;background:var(--blue)"></div>
  <div class="photo" role="img" aria-label="Team photo of Henrik Adler" style="left:51px;top:79px;width:83px;height:100px;border:2px solid #fff;box-shadow:0 1px 4px rgba(0,0,0,.4)"></div>
  <div class="photo warm" role="img" aria-label="Team photo of Marlene K. Osterwald" style="left:169px;top:79px;width:83px;height:100px;border:2px solid #fff;box-shadow:0 1px 4px rgba(0,0,0,.4)"></div>
  <div class="photo dark" role="img" aria-label="Team photo of dr Tobias Kern" style="left:288px;top:79px;width:83px;height:100px;border:2px solid #fff;box-shadow:0 1px 4px rgba(0,0,0,.4)"></div>
</section>

<section class="slide col-l" style="top:1683px">
  <h2 class="h-title" style="left:33px;top:23px;font-size:19px;line-height:1.2">ABOUT<br>OUR<br>BUSINESS</h2>
  <p class="tiny" style="position:absolute;left:33px;top:110px;width:80px;text-align:justify;color:#888">At vero eos et accusamus et iusto odio dignissimos ducimus qui blanditiis praesentium voluptatum deleniti atque corrupti quos dolores et quas molestias excepturi sint occaecati cupiditate non provident, similique sunt in culpa qui officia deserunt mollitia animi, id est laborum et dolorum fuga harum quidem.</p>
  <div class="photo" role="img" aria-label="Photo of a young man in a grey t-shirt with crossed arms" style="left:130px;top:0;width:130px;height:237px;background:linear-gradient(170deg,#d9d9d9,#8b8b8b)"></div>
  <div style="position:absolute;left:265px;top:42px;width:145px">
    <div style="display:flex;gap:30px;align-items:flex-start;margin-bottom:30px"><span style="width:16px;height:16px;border-radius:50%;background:var(--blue);flex:none;margin-top:10px"></span><p class="tiny" style="color:#999">At vero eos et accusamus et iusto odio dignissimos ducimus qui.</p></div>
    <div style="display:flex;gap:30px;align-items:flex-start;margin-bottom:30px"><span style="width:16px;height:16px;border-radius:50%;background:var(--blue);flex:none;margin-top:10px"></span><p class="tiny" style="color:#999">At vero eos et accusamus et iusto odio dignissimos ducimus qui.</p></div>
    <div style="display:flex;gap:30px;align-items:flex-start"><span style="width:16px;height:16px;border-radius:50%;background:var(--blue);flex:none;margin-top:10px"></span><p class="tiny" style="color:#999">At vero eos et accusamus et iusto odio dignissimos ducimus qui.</p></div>
  </div>
</section>

<section class="slide col-r" style="top:1683px">
  <div style="position:absolute;right:0;top:0;width:210px;height:237px;background:var(--panel)"></div>
  <h2 style="position:absolute;left:0;width:421px;text-align:center;top:38px;font-family:'Fira Sans',sans-serif;font-weight:600;font-size:17px;color:#222">TABLE OF CONTENT</h2>
  <div class="toc-item" style="left:43px;top:84px"><div class="toc-num">01</div><div><h5>Section here</h5><p>Lorem ipsum dolor sit amet, consectetur adipiscing elit.</p></div></div>
  <div class="toc-item" style="left:43px;top:126px"><div class="toc-num">02</div><div><h5>Section here</h5><p>Lorem ipsum dolor sit amet, consectetur adipiscing elit.</p></div></div>
  <div class="toc-item" style="left:43px;top:168px"><div class="toc-num">03</div><div><h5>Section here</h5><p>Lorem ipsum dolor sit amet, consectetur adipiscing elit.</p></div></div>
  <div class="toc-item" style="left:233px;top:84px"><div class="toc-num">04</div><div><h5>Section here</h5><p>Lorem ipsum dolor sit amet, consectetur adipiscing elit.</p></div></div>
  <div class="toc-item" style="left:233px;top:126px"><div class="toc-num">05</div><div><h5>Section here</h5><p>Lorem ipsum dolor sit amet, consectetur adipiscing elit.</p></div></div>
  <div class="toc-item" style="left:233px;top:168px"><div class="toc-num">06</div><div><h5>Section here</h5><p>Lorem ipsum dolor sit amet, consectetur adipiscing elit.</p></div></div>
</section>

<section class="slide col-l" style="top:1949px">
  <h2 style="position:absolute;left:47px;top:42px;font-family:'Fira Sans',sans-serif;font-weight:500;font-size:18px;line-height:1.3">Welcome<br>Message</h2>
  <p class="tiny" style="position:absolute;left:47px;top:100px;width:100px;color:#888">Lorem ipsum dolor sit amet, consectetur adipiscing elit, sed do eiusmod tempor incididunt ut labore et dolore magna aliqua. Ut enim ad minim veniam, quis nostrud exercitation.</p>
  <div class="btn" style="left:44px;top:174px;width:67px;height:17px;line-height:17px;font-size:7.5px;border-radius:9px">Read More</div>
  <div class="brand" style="position:absolute;left:190px;top:100px;width:225px;text-align:left">
    <div class="brand-name" style="color:var(--blue);font-size:19px">LANTERN WEAVERS</div>
  </div>
  <p class="tiny" style="position:absolute;left:190px;top:142px;width:190px;color:#888">Lorem ipsum dolor sit amet, consectetur adipiscing elit, sed do eiusmod tempor incididunt ut labore et dolore magna aliqua. Ut enim ad minim veniam, quis nostrud exercitation ullamco laboris nisi ut aliquip ex ea commodo consequat. Duis aute irure dolor in reprehenderit in voluptate velit esse cillum dolore eu fugiat nulla pariatur.</p>
</section>

<section class="slide blue col-r" style="top:1949px">
  <h2 style="position:absolute;left:0;width:421px;text-align:center;top:42px;font-family:'Fira Sans',sans-serif;font-weight:400;font-size:35px;line-height:1.2">Thanks<br>For Wathing</h2>
  <div style="position:absolute;left:0;width:421px;text-align:center;top:148px;font-size:10px;line-height:1.4">Harbor City, Westland<br>P : +00 4 0000 1234 &nbsp;E : info@lanternweavers.example<br>www.lanternweavers.example</div>
</section>

</body>
</html>
```